Corporate brochure Velorin consulting

I am a business law and taxation law firm. I would like to create a super sharp and modern catalogue that really describes our values and the services we offer among other things. It has to be bilingual. I dont want it to look like old fashioned typical law firms. Here are some characteristics of the catalogue:

- size: 8.5 x 11 landscape
- 20 pages in total including the cover page
- bilingual catalogue

Our corporate colors are the ones used in the logo attached.

I already have purchased all of the photos needed for the project.Please see attached document for a detailed description of the project.

I have pictures that I can email you for the project. just email me at jbarlow@velorin-example.ca and I will send the file.

I would just like for you to make available the text boxes on each page and then I will provide the text once Im finished.

Target Market(s)

business owners and professionals

Industry/Entity Type

Business

Font styles to use
Sans Serif

Colors
0692cd
f37122

Requirements
Must have
• bold fonts, very clean white backgrounds, modern and yet very edgy design
• each page should have a large enough area to add text.
• ***I like as the titles: all in large letters and font to use is Adequate,
• Large titles on the left side of page in orange and right side in blue
• for the text: font to be used is asenine
• page numbering should be very visible in the middle of the page left and right and not on bottom or upper corners.
Nice to have
• I like the use of metallic silvers . Not all of the pictures need to be used its the choic of the designer.

```html
<!DOCTYPE html>
<html lang="en">
<head>
<meta charset="UTF-8">
<title>Velorin — About Us / À propos</title>
<link rel="stylesheet" href="https://fonts.googleapis.com/css2?family=Jost:wght@400;500;600;700&display=swap">
<style>
  :root {
    --orange: #f37122;
    --blue: #0692cd;
    --silver: #b9b9b9;
    --ink: #2b2b2b;
    --paper: #f3f3f3;
    --paper-edge: #e4e4e4;
    --white: #ffffff;
    --photo-stone: #c9c9c9;
    --photo-stone-dark: #8f8f8f;
    --photo-library: #6e4a34;
    --photo-library-light: #b7a08a;
  }
  * { margin: 0; padding: 0; box-sizing: border-box; }
  html, body { width: 1200px; height: 776px; overflow: hidden; }
  body {
    background: linear-gradient(180deg, var(--paper-edge) 0%, var(--paper) 40%, var(--paper) 100%);
    font-family: "Jost", "Century Gothic", sans-serif;
    position: relative;
  }
  .spread { position: absolute; inset: 0; }
  .page-fold {
    position: absolute; left: 600px; top: 0; width: 1px; height: 776px;
    background: rgba(0,0,0,0.06);
  }
  .folio {
    position: absolute; top: 0; width: 26px; height: 20px;
    color: var(--white); font-size: 9px; font-weight: 500;
    display: flex; align-items: center; justify-content: center;
  }
  .folio--left { left: 288px; background: var(--orange); }
  .folio--right { left: 879px; background: var(--blue); }
  .folio-brand {
    position: absolute; top: 23px; width: 60px; text-align: center;
    font-size: 7px; font-weight: 500; color: #7a7a7a; letter-spacing: 0.5px;
  }
  .folio-brand--left { left: 271px; }
  .folio-brand--right { left: 862px; }
  .accent-bar { position: absolute; top: 115px; height: 15px; }
  .accent-bar.blue { background: var(--blue); }
  .accent-bar.silver { background: var(--silver); }
  .accent-bar.orange { background: var(--orange); }
  .text-panel {
    position: absolute; top: 137px; height: 580px;
    color: var(--white); padding: 12px 18px 0 38px;
  }
  .text-panel--left { left: 0; width: 354px; background: var(--orange); }
  .text-panel--right { left: 600px; width: 310px; background: var(--blue); padding-left: 36px; }
  .section-title {
    font-size: 31px; font-weight: 500; letter-spacing: 0.3px; line-height: 1;
    display: flex; align-items: center; gap: 8px; margin-left: -14px; margin-bottom: 18px;
  }
  .section-title svg { width: 14px; height: 17px; flex: none; }
  .body-copy {
    font-size: 11.6px; font-weight: 600; line-height: 16.6px;
  }
  .photo { position: absolute; width: 200px; }
  .photo--columns {
    top: 137px; height: 88px;
    background: linear-gradient(90deg, var(--photo-stone) 0%, #efefef 30%, var(--photo-stone-dark) 55%, #e6e6e6 80%, var(--photo-stone) 100%);
  }
  .photo--office {
    top: 233px; height: 150px;
    background: linear-gradient(180deg, var(--photo-library) 0%, var(--photo-library-light) 55%, #e9e9e9 100%);
  }
  .col-left { left: 364px; }
  .col-right { left: 964px; }
  .pull-quote {
    position: absolute; top: 380px; width: 190px;
  }
  .quote-mark {
    font-size: 54px; font-weight: 700; line-height: 1; font-family: Georgia, serif;
  }
  .quote-mark--open { height: 30px; }
  .quote-mark--close { position: absolute; right: -4px; top: 252px; }
  .pull-quote--left .quote-mark { color: var(--orange); }
  .pull-quote--right .quote-mark { color: var(--blue); }
  .quote-text {
    font-size: 18.5px; font-weight: 600; line-height: 24px; color: var(--ink);
  }
</style>
</head>
<body>
<main class="spread">
  <div class="page-fold"></div>

  <div class="folio folio--left">01</div>
  <div class="folio-brand folio-brand--left">Velorin</div>
  <div class="folio folio--right">02</div>
  <div class="folio-brand folio-brand--right">Velorin</div>

  <div class="accent-bar blue" style="left:189px;width:42px"></div>
  <div class="accent-bar silver" style="left:236px;width:43px"></div>
  <div class="accent-bar orange" style="left:283px;width:315px"></div>
  <div class="accent-bar blue" style="left:602px;width:316px"></div>
  <div class="accent-bar silver" style="left:923px;width:42px"></div>
  <div class="accent-bar orange" style="left:972px;width:42px"></div>

  <section class="text-panel text-panel--left" lang="en">
    <h1 class="section-title"><svg viewBox="0 0 14 17"><polygon points="0,0 14,8.5 0,17" fill="#fff"/></svg>ABOUT US</h1>
    <p class="body-copy">Lorem ipsum dolor sit amet, consectetuer adipiscing elit, sed diam nonummy nibh euismod tincidunt ut laoreet dolore magna aliquam erat volutpat. Ut wisi enim ad minim veniam, quis nostrud exerci tation ullamcorper suscipit lobortis nisl ut aliquip ex ea commodo consequat. Duis autem vel eum iriure dolor in hendrerit in vulputate velit esse molestie consequat, vel illum dolore eu feugiat nulla facilisis at vero eros et accumsan et iusto odio dignissim qui blandit praesent luptatum zzril delenit augue duis dolore te feugait nulla facilisi. Nam liber tempor cum soluta nobis eleifend option congue nihil imperdiet doming id quod mazim placerat facer possim assum. Typi non habent claritatem insitam; est usus legentis in iis qui facit</p>
  </section>

  <div class="photo photo--columns col-left" role="img" aria-label="Photo of classical stone columns"></div>
  <div class="photo photo--office col-left" role="img" aria-label="Photo of a lawyer working at a laptop in front of law bookshelves"></div>

  <blockquote class="pull-quote pull-quote--left col-left">
    <div class="quote-mark quote-mark--open">&ldquo;</div>
    <p class="quote-text">Lorem ipsum dolor sit amet, consectetuer adipiscing elit, sed diam nonummy nibh euismod tincidunt ut laoreet dolore magna aliquam erat volutpat.</p>
    <div class="quote-mark quote-mark--close">&rdquo;</div>
  </blockquote>

  <section class="text-panel text-panel--right" lang="fr">
    <h1 class="section-title"><svg viewBox="0 0 14 17"><polygon points="0,0 14,8.5 0,17" fill="#fff"/></svg>À PROPOS</h1>
    <p class="body-copy">Lorem ipsum dolor sit amet, consectetuer adipiscing elit, sed diam nonummy nibh euismod tincidunt ut laoreet dolore magna aliquam erat volutpat. Ut wisi enim ad minim veniam, quis nostrud exerci tation ullamcorper suscipit lobortis nisl ut aliquip ex ea commodo consequat. Duis autem vel eum iriure dolor in hendrerit in vulputate velit esse molestie consequat, vel illum dolore eu feugiat nulla facilisis at vero eros et accumsan et iusto odio dignissim qui blandit praesent luptatum zzril delenit augue duis dolore te feugait nulla facilisi. Nam liber tempor cum soluta nobis eleifend option congue nihil imperdiet doming id quod mazim placerat facer possim assum. Typi non habent claritatem insitam; est usus legentis in iis qui facit</p>
  </section>

  <div class="photo photo--columns col-right" role="img" aria-label="Photo of classical stone columns"></div>
  <div class="photo photo--office col-right" role="img" aria-label="Photo of a lawyer working at a laptop in front of law bookshelves"></div>

  <blockquote class="pull-quote pull-quote--right col-right">
    <div class="quote-mark quote-mark--open">&ldquo;</div>
    <p class="quote-text">Lorem ipsum dolor sit amet, consectetuer adipiscing elit, sed diam nonummy nibh euismod tincidunt ut laoreet dolore magna aliquam erat volutpat.</p>
    <div class="quote-mark quote-mark--close">&rdquo;</div>
  </blockquote>
</main>
</body>
</html>
```